KAV cards & more
Business cards, fax cover sheet, letterhead, envelopes, powerpoint slide template
Modern
Tad Willers
Owner
17 Lindgate Row Bedminster, NJ 07921
twkav@mailvane.net
Please integrate my already-completed company logo (attached) in a clean, modern design for business cards, Fax cover sheet, letterhead, envelopes, and powerpoint slide template

```html
<!DOCTYPE html>
<html lang="en">
<head>
<meta charset="utf-8">
<title>KAV stationery set</title>
<link href="https://fonts.googleapis.com/css2?family=Exo+2:wght@400;800&family=Open+Sans:wght@400;600&display=swap" rel="stylesheet">
<style>
:root{
  --green-dark:#1f6e12;
  --green:#3a9a1c;
  --green-light:#9bd23c;
  --green-pale:#e6f3dc;
  --ink:#5a5a5a;
  --line:#c9c9c9;
  --paper:#ffffff;
  --bg:#ffffff;
}
*{box-sizing:border-box;margin:0;padding:0}
html,body{width:1200px;height:504px;overflow:hidden;background:var(--bg);font-family:"Open Sans",sans-serif;color:var(--ink)}
.canvas{position:relative;width:1200px;height:504px}
.sheet{position:absolute;background:var(--paper);box-shadow:0 2px 6px rgba(0,0,0,.18);overflow:hidden}
.sheet::after{content:"";position:absolute;left:10%;right:10%;bottom:0;height:3px;background:radial-gradient(ellipse at center,var(--green-light),transparent 70%)}
.brand{position:absolute;display:flex;align-items:center;gap:5px}
.brand-dot{width:18px;height:18px;border-radius:50%;background:var(--green)}
.brand-name{font-family:"Exo 2",sans-serif;font-weight:800;font-size:20px;color:var(--green);letter-spacing:2px;line-height:1}
.addr{position:absolute;font-size:4.5px;line-height:6px;color:var(--ink);white-space:nowrap}
.mark{position:absolute;display:flex;align-items:center;justify-content:center;gap:10px;opacity:.12}
.mark .brand-dot{width:56px;height:56px}
/* fax */
.fax{left:24px;top:12px;width:312px;height:444px}
.fax-title{position:absolute;right:14px;top:54px;font-size:16px;line-height:16px;letter-spacing:1px;color:#444}
.fax-table{position:absolute;left:12px;top:78px;width:288px;border-collapse:collapse;font-size:5px}
.fax-table td{border:1px solid var(--line);height:16px;padding:0 4px}
.fax-table .label{background:#f1f1f1;width:40px}
.fax-checks{position:absolute;left:12px;top:152px;display:flex;gap:20px;font-size:5px}
.fax-checks span::before{content:"";display:inline-block;width:5px;height:5px;border:1px solid #999;margin-right:3px;vertical-align:-1px}
.fax-comments{position:absolute;left:12px;top:170px;font-size:5px}
/* envelopes */
.env-back{left:355px;top:12px;width:340px;height:112px}
.env-flap{position:absolute;inset:0}
.env-badge{position:absolute;left:155px;top:24px;width:30px;height:30px;border-radius:50%;background:var(--paper)}
.env-front{left:355px;top:132px;width:340px;height:168px}
.env-small{left:355px;top:324px;width:340px;height:132px}
/* letterhead */
.letter{left:715px;top:12px;width:318px;height:444px}
/* cards */
.card{position:absolute;box-shadow:0 2px 5px rgba(0,0,0,.2);overflow:hidden}
.card-white{background:var(--paper)}
.card-green{background:radial-gradient(circle at 50% 50%,var(--green-light),var(--green) 45%,var(--green-dark))}
.card-front{left:1037px;top:12px;width:140px;height:84px}
.card-back{left:1037px;top:100px;width:140px;height:86px}
.card-tall-green{left:1039px;top:211px;width:58px;height:137px}
.card-tall-white{left:1099px;top:211px;width:78px;height:137px}
.card-name{position:absolute;font-size:5px;font-weight:600;color:#333;white-space:nowrap}
.card-role{position:absolute;font-size:4px;color:var(--ink);white-space:nowrap}
.on-green .brand-name{color:var(--paper)}
.on-green .brand-dot{background:var(--paper)}
.small .brand-name{font-size:12px;letter-spacing:1px}
.small .brand-dot{width:11px;height:11px}
</style>
</head>
<body>
<main class="canvas">

  <section class="sheet fax" aria-label="Fax cover sheet">
    <div class="brand" style="left:12px;top:10px"><span class="brand-dot"></span><span class="brand-name">KAV</span></div>
    <div class="addr" style="left:100px;top:12px">17 Lindgate Row Bedminster, NJ 07921<br>T 908 555 0142 F 908 555 0143<br>twkav@mailvane.net</div>
    <div class="fax-title">FAX</div>
    <table class="fax-table">
      <tr><td class="label">To</td><td></td><td class="label">From</td><td></td></tr>
      <tr><td class="label">Fax</td><td></td><td class="label">Pages</td><td></td></tr>
      <tr><td class="label">Phone</td><td></td><td class="label">Date</td><td></td></tr>
      <tr><td class="label">Re</td><td></td><td class="label">CC</td><td></td></tr>
    </table>
    <div class="fax-checks"><span>Urgent</span><span>For Review</span><span>Please Comment</span><span>Please Reply</span><span>Please Recycle</span></div>
    <div class="fax-comments">Comments:</div>
    <div class="mark" style="left:120px;top:240px"><span class="brand-dot"></span></div>
  </section>

  <section class="sheet env-back" aria-label="Envelope back">
    <svg class="env-flap" viewBox="0 0 340 112" preserveAspectRatio="none">
      <defs>
        <radialGradient id="flapGlow" cx="50%" cy="90%" r="70%">
          <stop offset="0" stop-color="#9bd23c"/>
          <stop offset=".5" stop-color="#3a9a1c"/>
          <stop offset="1" stop-color="#1f6e12"/>
        </radialGradient>
      </defs>
      <polygon points="0,0 340,0 170,104" fill="url(#flapGlow)"/>
    </svg>
    <div class="env-badge"></div>
  </section>

  <section class="sheet env-front" aria-label="Envelope front">
    <div class="brand small" style="left:12px;top:50px"><span class="brand-dot"></span><span class="brand-name">KAV</span></div>
    <div class="addr" style="left:12px;top:148px">17 Lindgate Row Bedminster, NJ 07921</div>
  </section>

  <section class="sheet env-small" aria-label="Small envelope">
    <div class="addr" style="left:120px;top:36px">17 Lindgate Row<br>Bedminster, NJ 07921</div>
    <div class="mark" style="left:240px;top:46px"><span class="brand-dot"></span></div>
  </section>

  <section class="sheet letter" aria-label="Letterhead">
    <div class="brand" style="left:12px;top:10px"><span class="brand-dot"></span><span class="brand-name">KAV</span></div>
    <div class="addr" style="left:100px;top:12px">17 Lindgate Row Bedminster, NJ 07921<br>T 908 555 0142<br>twkav@mailvane.net</div>
    <div class="mark" style="left:120px;top:216px"><span class="brand-dot"></span></div>
  </section>

  <section class="card card-white card-front" aria-label="Business card front">
    <div class="brand small" style="left:8px;top:10px"><span class="brand-dot"></span><span class="brand-name">KAV</span></div>
    <div class="card-name" style="left:96px;top:8px">Tad Willers</div>
    <div class="card-role" style="left:96px;top:15px">Owner</div>
    <div class="card-role" style="left:8px;top:66px">17 Lindgate Row Bedminster, NJ 07921</div>
    <div class="card-role" style="left:8px;top:72px">twkav@mailvane.net</div>
  </section>

  <section class="card card-green card-back on-green" aria-label="Business card back">
    <div class="brand small" style="left:44px;top:36px"><span class="brand-dot"></span><span class="brand-name">KAV</span></div>
  </section>

  <section class="card card-green card-tall-green on-green" aria-label="Vertical card back">
    <div class="brand small" style="left:7px;top:62px"><span class="brand-dot"></span><span class="brand-name">KAV</span></div>
  </section>

  <section class="card card-white card-tall-white" aria-label="Vertical card front">
    <div class="card-name" style="left:8px;top:8px">Tad Willers</div>
    <div class="card-role" style="left:8px;top:15px">Owner</div>
    <div class="card-role" style="left:8px;top:116px">17 Lindgate Row</div>
    <div class="card-role" style="left:8px;top:122px">twkav@mailvane.net</div>
  </section>

  <div class="brand small" style="left:1056px;top:432px"><span class="brand-dot"></span><span class="brand-name">KAV</span></div>

</main>
</body>
</html>
```